Business Card for Industrial Distributor

We need a business card design for an industrial distributor. We sell machine parts for the manufacturing and oil industry. We would like the cards to look clean and modern but with a touch of industry.

Our colors are blue/white.

Please feel free to visit our website www.krovelmint.com

Target Market(s)

mexican manufacturers in the automobile/aerospace industry

Industry/Entity Type

Industrial

Colors
ffffff
0555a3

```html
<!DOCTYPE html>
<html lang="en">
<head>
<meta charset="utf-8">
<title>Krovelmint Business Card</title>
<link rel="stylesheet" href="https://fonts.googleapis.com/css2?family=Open+Sans:ital,wght@0,400;0,600;0,700;0,800;1,400&display=swap">
<style>
  :root {
    --page-bg: #d2d2d2;
    --card-white: #ffffff;
    --brand-navy: #2e3192;
    --brand-blue: #0555a3;
    --brand-bright: #1679c4;
    --text-grey: #4a4a4a;
    --rule-grey: #c9c9c9;
  }
  * { margin: 0; padding: 0; box-sizing: border-box; }
  html, body {
    width: 1200px; height: 987px; overflow: hidden;
    background: var(--page-bg);
    font-family: "Open Sans", Arial, sans-serif;
  }
  .card {
    position: absolute; left: 293px; width: 615px; height: 351px;
    border-radius: 16px; overflow: hidden;
  }
  .card-front { top: 130px; background: var(--card-white); }
  .card-back {
    top: 505px;
    background: radial-gradient(ellipse at 35% 30%, var(--brand-bright) 0%, var(--brand-blue) 45%, var(--brand-navy) 100%);
  }
  .front-wordmark {
    position: absolute; left: 42px; top: 177px; transform: translateY(-50%);
    display: flex; align-items: center; gap: 10px;
  }
  .front-wordmark .dot {
    width: 34px; height: 34px; border-radius: 50%; background: var(--brand-blue);
  }
  .front-wordmark .name {
    font-size: 38px; font-weight: 800; color: var(--brand-navy); letter-spacing: -0.5px;
  }
  .divider {
    position: absolute; left: 328px; top: 57px; width: 1px; height: 241px;
    background: var(--rule-grey);
  }
  .contact { position: absolute; left: 355px; top: 64px; color: var(--text-grey); }
  .person-name { font-size: 21px; font-weight: 700; color: var(--brand-navy); line-height: 1.2; }
  .person-title { font-size: 16px; line-height: 1.3; margin-bottom: 9px; }
  .company { font-size: 16px; font-weight: 600; line-height: 1.35; }
  .address { font-size: 16px; line-height: 1.35; margin-bottom: 9px; }
  .lines { list-style: none; }
  .lines li { display: flex; align-items: center; gap: 9px; font-size: 16px; line-height: 24px; }
  .lines svg { width: 14px; height: 14px; fill: var(--brand-navy); flex: none; }
  .front-rule {
    position: absolute; left: 0; right: 0; top: 322px; height: 2px; background: #aab4cf;
  }
  .front-band {
    position: absolute; left: 0; right: 0; top: 327px; bottom: 0;
    background: linear-gradient(90deg, var(--brand-navy) 0%, var(--brand-bright) 50%, var(--brand-navy) 100%);
  }
  .back-decoration {
    position: absolute; right: 0; top: 0; width: 330px; height: 100%;
    background: linear-gradient(200deg, #ffffff 0%, #e6eef8 55%, rgba(255,255,255,0) 100%);
  }
  .back-wordmark {
    position: absolute; left: 34px; bottom: 54px;
    font-size: 40px; font-weight: 800; color: var(--card-white); letter-spacing: -0.5px;
  }
  .back-web {
    position: absolute; left: 36px; bottom: 20px;
    font-size: 15px; font-style: italic; color: var(--card-white); letter-spacing: 3px;
  }
</style>
</head>
<body>
  <section class="card card-front">
    <div class="front-wordmark">
      <span class="dot"></span>
      <span class="name">Krovelmint</span>
    </div>
    <div class="divider"></div>
    <div class="contact">
      <p class="person-name">DANIEL REYES</p>
      <p class="person-title">CEO/Founder</p>
      <p class="company">Krovelmint International Corp.</p>
      <p class="address">4820 Calloway Ridge Rd.<br>Harlow.TX 78590</p>
      <ul class="lines">
        <li><svg viewBox="0 0 16 16"><path d="M3.6 1.2l2.2 2.9-1.2 1.6c.9 2 2.5 3.6 4.5 4.5l1.6-1.2 2.9 2.2-1.2 2.6C7.2 14 2 8.8 1 3.4z"/></svg>(555) 318 - 2207</li>
        <li><svg viewBox="0 0 16 16"><path d="M4 1h8v4H4zM1 6h14v6h-2v3H3v-3H1zm4 5v3h6v-3z"/></svg>(555) 318 - 2214</li>
        <li><svg viewBox="0 0 16 16"><path d="M1 3h14v10H1zm1.5 1.2v.4L8 8.5l5.5-3.9v-.4zm0 2.1v5.5h11V6.3L8 10.2z"/></svg>sales@krovelmint.com</li>
        <li><svg viewBox="0 0 16 16"><path d="M8 1a7 7 0 1 0 0 14A7 7 0 0 0 8 1zm0 1.5c.8 0 1.7 1.8 2 4.5H6c.3-2.7 1.2-4.5 2-4.5zM2.6 9h2.9c.1 1.5.4 2.8.9 3.7A5.5 5.5 0 0 1 2.6 9zm3 -2H2.6a5.5 5.5 0 0 1 3.8-3.7C6 4.2 5.7 5.5 5.6 7zm4.8 0c-.1-1.5-.4-2.8-.9-3.7A5.5 5.5 0 0 1 13.4 7zM6 9h4c-.3 2.7-1.2 4.5-2 4.5S6.3 11.7 6 9zm3.6 3.7c.5-.9.8-2.2.9-3.7h2.9a5.5 5.5 0 0 1-3.8 3.7z"/></svg>www.krovelmint.com</li>
      </ul>
    </div>
    <div class="front-rule"></div>
    <div class="front-band"></div>
  </section>

  <section class="card card-back">
    <div class="back-decoration" role="img" aria-label="Large brand symbol decoration area"></div>
    <p class="back-wordmark">Krovelmint</p>
    <p class="back-web">www.krovelmint.com</p>
  </section>
</body>
</html>
```